Harlow Mesa Podiatry
Business card, letterhead & envelope
Professional
4631 NW 52nd St
Suite 310
Summerfield, FL 32786
mtollanddpm@brindlemail.com
Front of Card should also have names of doctors:
Marcus Tolland, DPM
Lanh T. Vu, DPM
Back of card should have information for appointment:
1. Date
2. Time
3. Day of week to circle (ie Mon, Tues, Wed, Thurs, Fri)
4. "If unable to keep appointment kindly give 24 hours notice"
Logo designs for Harlow Mesa Podiatry

```html
<!DOCTYPE html>
<html lang="en">
<head>
<meta charset="utf-8">
<title>Harlow Mesa Podiatry — Stationery</title>
<link rel="stylesheet" href="https://fonts.googleapis.com/css2?family=Montserrat:wght@700;800&family=Open+Sans:wght@400;600&display=swap">
<style>
  :root {
    --board: #d9d9d9;
    --paper: #ffffff;
    --green: #6cb33f;
    --green-light: #a6d37f;
    --ink: #333333;
    --ink-soft: #666666;
    --faint: #e7e7e7;
    --card-dark: #1f1f1f;
    --rule: #8a8a8a;
  }
  * { box-sizing: border-box; margin: 0; padding: 0; }
  html, body { width: 1200px; height: 725px; overflow: hidden; }
  body { background: var(--board); font-family: "Open Sans", Arial, sans-serif; color: var(--ink); position: relative; }

  .sheet { position: absolute; background: var(--paper); overflow: hidden; box-shadow: 0 1px 3px rgba(0,0,0,.18); }
  .sheet svg.swoosh { position: absolute; left: 0; bottom: 0; width: 100%; }

  .brand { position: absolute; display: flex; align-items: center; gap: 6px; }
  .brand-mark { background: var(--green); flex: none; }
  .brand-name { font-family: "Montserrat", Arial, sans-serif; font-weight: 800; color: var(--ink); line-height: .95; text-transform: uppercase; letter-spacing: .02em; }

  .watermark { position: absolute; left: 0; right: 0; text-align: center; font-family: "Montserrat", Arial, sans-serif; font-weight: 800; color: var(--faint); text-transform: uppercase; line-height: .95; letter-spacing: .03em; }

  .contact { position: absolute; color: var(--ink); line-height: 1.35; }
  .address { position: absolute; color: #fff; line-height: 1.35; text-align: left; }

  /* Letterhead */
  .letterhead { left: 211px; top: 36px; width: 377px; height: 660px; }
  .letterhead .brand { left: 14px; top: 10px; }
  .letterhead .brand-mark { width: 14px; height: 30px; }
  .letterhead .brand-name { font-size: 12px; }
  .letterhead .watermark { top: 330px; font-size: 44px; }
  .letterhead .contact { left: 14px; bottom: 14px; font-size: 7px; }
  .letterhead .address { right: 20px; bottom: 14px; font-size: 7px; }

  /* Envelope */
  .envelope { left: 643px; top: 36px; width: 533px; height: 324px; }
  .envelope .brand { left: 22px; top: 26px; }
  .envelope .brand-mark { width: 16px; height: 34px; }
  .envelope .brand-name { font-size: 14px; }
  .envelope .watermark { top: 80px; font-size: 30px; left: 150px; right: 150px; }
  .envelope .contact { left: 22px; bottom: 46px; font-size: 7px; }
  .envelope .address { right: 46px; bottom: 58px; font-size: 7px; }

  /* Business card back */
  .card-back { left: 12px; top: 187px; width: 192px; height: 125px; display: flex; }
  .card-back .panel-brand { width: 52px; background: var(--green); position: relative; }
  .card-back .brand { left: 6px; top: 8px; flex-direction: column; align-items: flex-start; gap: 4px; }
  .card-back .brand-mark { width: 10px; height: 20px; background: #fff; }
  .card-back .brand-name { font-size: 7.5px; color: #fff; }
  .card-back .panel-appointment { flex: 1; background: var(--card-dark); padding: 6px 8px 6px; color: #ddd; font-size: 5.5px; }
  .appt-field { display: flex; align-items: flex-end; gap: 4px; height: 13px; }
  .appt-field .label { flex: none; width: 24px; }
  .appt-field .line { flex: 1; border-bottom: 1px solid var(--rule); }
  .appt-days { display: flex; justify-content: space-between; margin-top: 7px; }
  .appt-note { margin-top: 7px; font-size: 5px; line-height: 1.35; color: #bbb; }

  /* Business card front */
  .card-front { left: 12px; top: 317px; width: 192px; height: 125px; }
  .card-front .brand { left: 8px; top: 8px; }
  .card-front .brand-mark { width: 9px; height: 20px; }
  .card-front .brand-name { font-size: 8px; }
  .card-front .doctors { position: absolute; right: 8px; top: 10px; font-size: 5px; line-height: 1.4; color: var(--ink); text-align: left; }
  .card-front .contact { left: 8px; top: 58px; font-size: 4.6px; }
  .card-front .address { right: 8px; top: 58px; font-size: 4.6px; color: var(--ink); }
</style>
</head>
<body>

  <section class="sheet letterhead">
    <div class="brand">
      <span class="brand-mark"></span>
      <span class="brand-name">Harlow<br>Mesa<br>Podiatry</span>
    </div>
    <div class="watermark">Harlow<br>Mesa<br>Podiatry</div>
    <svg class="swoosh" viewBox="0 0 377 150" height="150" preserveAspectRatio="none" aria-hidden="true">
      <path d="M0 140 Q190 138 377 28 L377 44 Q190 146 0 146 Z" fill="var(--green-light)"/>
      <path d="M0 146 Q200 144 377 44 L377 150 L0 150 Z" fill="var(--green)"/>
    </svg>
    <div class="contact">Phone: (352) 555-0148<br>mtollanddpm@brindlemail.com</div>
    <div class="address">4631 NW 52nd St, Suite 310<br>Summerfield, FL 32786</div>
  </section>

  <section class="sheet envelope">
    <div class="brand">
      <span class="brand-mark"></span>
      <span class="brand-name">Harlow<br>Mesa<br>Podiatry</span>
    </div>
    <div class="watermark">Harlow<br>Mesa<br>Podiatry</div>
    <svg class="swoosh" viewBox="0 0 533 180" height="180" preserveAspectRatio="none" aria-hidden="true">
      <path d="M0 150 Q300 150 533 18 L533 30 Q300 160 0 160 Z" fill="var(--green-light)"/>
      <path d="M0 160 Q310 158 533 30 L533 180 L0 180 Z" fill="var(--green)"/>
    </svg>
    <div class="contact">Phone: (352) 555-0148<br>mtollanddpm@brindlemail.com</div>
    <div class="address">4631 NW 52nd St, Suite 310<br>Summerfield, FL 32786</div>
  </section>

  <section class="sheet card-back">
    <div class="panel-brand">
      <div class="brand">
        <span class="brand-mark"></span>
        <span class="brand-name">Harlow<br>Mesa<br>Podiatry</span>
      </div>
    </div>
    <div class="panel-appointment">
      <div class="appt-field"><span class="label">Patient</span><span class="line"></span></div>
      <div class="appt-field"><span class="label">Date</span><span class="line"></span></div>
      <div class="appt-field"><span class="label">Time</span><span class="line"></span></div>
      <div class="appt-field"><span class="label">Day</span><span class="line"></span></div>
      <div class="appt-days"><span>Mon</span><span>Tues</span><span>Wed</span><span>Thurs</span><span>Fri</span></div>
      <p class="appt-note">If unable to keep appointment<br>kindly give 24 hours notice</p>
    </div>
  </section>

  <section class="sheet card-front">
    <div class="brand">
      <span class="brand-mark"></span>
      <span class="brand-name">Harlow<br>Mesa<br>Podiatry</span>
    </div>
    <div class="doctors">Marcus Tolland, DPM<br>Lanh T. Vu, DPM</div>
    <svg class="swoosh" viewBox="0 0 192 50" height="50" preserveAspectRatio="none" aria-hidden="true">
      <path d="M0 40 Q110 40 192 12 L192 17 Q110 44 0 44 Z" fill="var(--green-light)"/>
      <path d="M0 44 Q110 44 192 17 L192 50 L0 50 Z" fill="var(--green)"/>
    </svg>
    <div class="contact">Phone: (352) 555-0148<br>mtollanddpm@brindlemail.com</div>
    <div class="address">4631 NW 52nd St, Suite 310<br>Summerfield, FL 32786</div>
  </section>

</body>
</html>
```